Traffic product supplier - Temporary Raised Pavement Markers

We need a flyer design that will grab the customer's eye to the product (TRPMs) and entice curiosity to the business. Showing 1 product but promoting other products. The following information should be included:
- Logo (attached)
- Sale Product image (Temporary Road Pavement Marker AKA Tack and Treads)
- Product wording (attached word document)

Happy for you to add/amend wording for grammatical purpose and other images that show it is a sale flyer.

Background on KRV - We are a thermoplastic manufacturer for road markings and traffic product supplier. KRV specializes in producing high quality hotmelt thermoplastic that meet Australian Standard AS7312.4. We are able to produce other specifications as required by the customer.

Would like the colour scheme to be similar to the logo.

If you need more information let me know.

Target Market(s)

Asphalt industry / road builders

Font styles to use
Serif
Sans Serif

Requirements
Must have
• - Kestrel Roadline Ventures (My company name)
- Contact details:
- 02 9471 2385
- marcus.t@krvsupply.com.au
- info@krvsupply.com.au
-www.krvlane.com

- Attached images.
-Title (Temporary Road Pavement Markers)

```html
<!DOCTYPE html>
<html lang="en">
<head>
<meta charset="utf-8">
<title>KRV – Temporary Road Pavement Markers</title>
<link rel="stylesheet" href="https://fonts.googleapis.com/css2?family=Montserrat:wght@400;500;600;700;800;900&display=swap">
<style>
  :root {
    --blue: #0f56a8;
    --blue-deep: #0a4590;
    --yellow: #fcc512;
    --grey: #c8c8c6;
    --ink: #1b1b1b;
    --ink-soft: #3a3a3a;
    --label: #6a6a6a;
    --white: #ffffff;
  }
  * { margin: 0; padding: 0; box-sizing: border-box; }
  html, body { width: 746px; height: 1200px; overflow: hidden; background: var(--white); }
  body { font-family: "Montserrat", Arial, sans-serif; color: var(--ink); }
  .flyer { position: relative; width: 746px; height: 1200px; overflow: hidden; background: var(--white); }

  .hero { position: absolute; left: 0; top: 0; width: 746px; height: 597px; }

  .brand { position: absolute; left: 30px; top: 36px; width: 290px; text-align: center; }
  .brand-name { display: inline-flex; align-items: center; gap: 10px; font-weight: 800; font-size: 64px; line-height: 1; color: var(--blue); letter-spacing: 2px; }
  .brand-name .mark { width: 22px; height: 22px; background: var(--yellow); }
  .brand-tagline { margin-top: 22px; font-size: 11px; font-weight: 600; color: var(--blue); }

  .title { position: absolute; left: 34px; top: 274px; font-weight: 800; line-height: 1; text-transform: uppercase; }
  .title span { display: block; white-space: nowrap; }
  .title .t1 { font-size: 44px; letter-spacing: 2.4px; color: var(--white); }
  .title .t2 { font-size: 94px; letter-spacing: 6px; color: var(--yellow); margin-top: -4px; }
  .title .t3 { font-size: 51px; letter-spacing: 1.6px; color: var(--white); margin-top: 0; }
  .title .t4 { font-size: 56px; letter-spacing: 3px; color: var(--yellow); margin-top: -2px; }

  .section-tag { position: absolute; left: 34px; height: 26px; display: flex; align-items: center; }
  .section-tag .label { background: var(--blue); color: var(--white); font-weight: 800; font-size: 19px; height: 26px; line-height: 26px; padding: 0 34px 0 12px; }
  .section-tag svg { margin-left: -14px; }
  .tag-about { top: 622px; }
  .tag-products { top: 749px; }

  .copy { position: absolute; left: 34px; width: 480px; font-size: 11.6px; font-weight: 500; line-height: 15.4px; color: var(--ink); }
  .copy-about { top: 667px; }
  .copy-products { top: 790px; }

  .features { position: absolute; left: 34px; top: 870px; list-style: none; font-size: 11.6px; font-weight: 500; color: var(--ink); }
  .features li { display: flex; align-items: center; gap: 8px; height: 23px; }

  .price { position: absolute; left: 34px; top: 992px; width: 472px; height: 64px; }
  .price-amount { position: absolute; left: 10px; top: 6px; font-weight: 800; font-size: 42px; color: var(--blue); line-height: 52px; }
  .price-amount sup { font-size: 20px; vertical-align: 20px; margin-right: 1px; }
  .price-unit { position: absolute; left: 170px; top: 0; line-height: 64px; font-weight: 800; font-size: 31px; color: var(--white); }

  .product { position: absolute; left: 575px; width: 150px; text-align: center; }
  .product .shot { width: 136px; height: 90px; margin: 0 auto; border-radius: 2px; }
  .product .name { margin-top: 12px; font-weight: 700; font-size: 14px; color: var(--label); }
  .product-red { top: 622px; }
  .product-red .shot { background: linear-gradient(180deg, #d8303a 0 12%, #efefef 12%, #d9d9d9 100%); }
  .product-white { top: 766px; }
  .product-white .shot { background: linear-gradient(180deg, #9aa0a8 0 12%, #f2f2f2 12%, #d6d6d6 100%); }
  .product-yellow { top: 924px; }
  .product-yellow .shot { background: linear-gradient(180deg, #f7d24a 0%, #e9b514 70%, #cfcfcf 100%); }

  .footer { position: absolute; left: 0; top: 1102px; width: 746px; height: 98px; }
  .contact { position: absolute; display: flex; flex-direction: column; gap: 4px; }
  .contact-direct { left: 34px; top: 1117px; color: var(--white); }
  .contact-general { left: 470px; top: 1118px; color: var(--ink-soft); }
  .contact .row { display: flex; align-items: center; gap: 12px; }
  .contact-direct .phone { font-weight: 800; font-size: 25px; line-height: 28px; }
  .contact-direct .email { font-weight: 600; font-size: 17px; line-height: 22px; }
  .contact-general .row span { font-weight: 500; font-size: 20px; line-height: 26px; }
</style>
</head>
<body>
<main class="flyer">

  <svg class="hero" viewBox="0 0 746 597">
    <defs>
      <linearGradient id="city-dusk" x1="0" y1="0" x2="0" y2="1">
        <stop offset="0" stop-color="#3f78b8"/>
        <stop offset="0.35" stop-color="#9fb9cc"/>
        <stop offset="0.55" stop-color="#44505c"/>
        <stop offset="1" stop-color="#2a2f3a"/>
      </linearGradient>
      <linearGradient id="panel-blue" x1="0" y1="0" x2="1" y2="1">
        <stop offset="0" stop-color="#0c4f9f"/>
        <stop offset="1" stop-color="#1160b5"/>
      </linearGradient>
    </defs>
    <rect width="746" height="597" fill="#ffffff"/>
    <polygon points="310,0 746,0 746,590 472,590" fill="url(#city-dusk)" role="img" aria-label="Photo of a city skyline at dusk with light trails on a highway"/>
    <polygon points="300,0 311,0 473,590 462,590" fill="var(--yellow)"/>
    <polygon points="0,196 354,196 356,202 0,202" fill="var(--yellow)"/>
    <polygon points="0,202 356,202 462,590 0,590" fill="url(#panel-blue)"/>
    <rect x="0" y="590" width="746" height="7" fill="var(--yellow)"/>
  </svg>

  <header class="brand">
    <div class="brand-name"><span class="mark"></span>KRV</div>
    <p class="brand-tagline">"Clear Lines for Every Journey Ahead"</p>
  </header>

  <h1 class="title">
    <span class="t1">Temporary</span>
    <span class="t2">Road</span>
    <span class="t3">Pavement</span>
    <span class="t4">Markers</span>
  </h1>

  <div class="section-tag tag-about">
    <span class="label">ABOUT US</span>
    <svg width="28" height="26" viewBox="0 0 28 26"><polygon points="0,0 14,0 24,13 14,26 0,26" fill="var(--blue)"/><polyline points="16,1 26,13 16,25" fill="none" stroke="var(--blue)" stroke-width="1.6"/></svg>
  </div>
  <p class="copy copy-about">Temporary road pavement markers, also known as tack ‘n’ treads, are a great short-term solution to mark asphalt and pavements before permanent line marking takes place. They provide a way to delineate lanes and edges before the permanent longitudinal line marking process takes place.</p>

  <div class="section-tag tag-products">
    <span class="label">PRODUCTS DITELES</span>
    <svg width="28" height="26" viewBox="0 0 28 26"><polygon points="0,0 14,0 24,13 14,26 0,26" fill="var(--blue)"/><polyline points="16,1 26,13 16,25" fill="none" stroke="var(--blue)" stroke-width="1.6"/></svg>
  </div>
  <p class="copy copy-products">TRPMs or tack ‘n’ treads are available in yellow or white and come with a Class 1A reflective strip applied to tough high impact plastic. They are an economical solution for making newly laid roads safer. An easy to remove clear cover protects the reflective film during sealing and is easily ripped off afterwards.</p>

  <ul class="features">
    <li><svg width="11" height="11" viewBox="0 0 11 11"><rect x="0.6" y="1.6" width="8.8" height="8.8" fill="none" stroke="var(--blue)" stroke-width="1.2"/><polyline points="2.5,5.5 5,8 10.5,1" fill="none" stroke="var(--blue)" stroke-width="1.4"/></svg>Dimensions: 100 mm long x 50 mm high x 25 mm wide</li>
    <li><svg width="11" height="11" viewBox="0 0 11 11"><rect x="0.6" y="1.6" width="8.8" height="8.8" fill="none" stroke="var(--blue)" stroke-width="1.2"/><polyline points="2.5,5.5 5,8 10.5,1" fill="none" stroke="var(--blue)" stroke-width="1.4"/></svg>Double sided Class 1A Reflective</li>
    <li><svg width="11" height="11" viewBox="0 0 11 11"><rect x="0.6" y="1.6" width="8.8" height="8.8" fill="none" stroke="var(--blue)" stroke-width="1.2"/><polyline points="2.5,5.5 5,8 10.5,1" fill="none" stroke="var(--blue)" stroke-width="1.4"/></svg>Clear cover for reflective protection</li>
    <li><svg width="11" height="11" viewBox="0 0 11 11"><rect x="0.6" y="1.6" width="8.8" height="8.8" fill="none" stroke="var(--blue)" stroke-width="1.2"/><polyline points="2.5,5.5 5,8 10.5,1" fill="none" stroke="var(--blue)" stroke-width="1.4"/></svg>Available in all white, and red (reflective strip) and white, all yellow and all blue</li>
  </ul>

  <div class="price">
    <svg width="472" height="64" viewBox="0 0 472 64">
      <polygon points="0,0 140,0 158,64 0,64" fill="var(--yellow)"/>
      <polygon points="136,0 472,0 472,64 154,64" fill="var(--blue)"/>
    </svg>
    <span class="price-amount"><sup>$</sup>0.40</span>
    <span class="price-unit">ex GST per TRPM</span>
  </div>

  <figure class="product product-red">
    <div class="shot" role="img" aria-label="Product photo of a temporary road pavement marker with red reflective strip"></div>
    <figcaption class="name">Temp RPM - Red</figcaption>
  </figure>
  <figure class="product product-white">
    <div class="shot" role="img" aria-label="Product photo of a white temporary road pavement marker"></div>
    <figcaption class="name">Temp RPM - White</figcaption>
  </figure>
  <figure class="product product-yellow">
    <div class="shot" role="img" aria-label="Product photo of a yellow temporary road pavement marker"></div>
    <figcaption class="name">Temp RPM - Yellow</figcaption>
  </figure>

  <svg class="footer" viewBox="0 0 746 98">
    <rect width="746" height="98" fill="var(--grey)"/>
    <polygon points="0,0 386,0 412,30 356,98 0,98" fill="var(--blue)"/>
  </svg>

  <div class="contact contact-direct">
    <div class="row phone">
      <svg width="18" height="18" viewBox="0 0 24 24"><path d="M6.6 10.8a15.1 15.1 0 0 0 6.6 6.6l2.2-2.2c.3-.3.7-.4 1-.2 1.1.4 2.3.6 3.6.6.6 0 1 .4 1 1V20c0 .6-.4 1-1 1A17 17 0 0 1 3 4c0-.6.4-1 1-1h3.5c.6 0 1 .4 1 1 0 1.3.2 2.5.6 3.6.1.3 0 .7-.2 1z" fill="var(--white)"/></svg>
      02 9471 2385
    </div>
    <div class="row email">
      <svg width="18" height="13" viewBox="0 0 18 13"><rect x="0.8" y="0.8" width="16.4" height="11.4" fill="none" stroke="var(--white)" stroke-width="1.6"/><polyline points="1,1 9,7.5 17,1" fill="none" stroke="var(--white)" stroke-width="1.6"/></svg>
      marcus.t@krvsupply.com.au
    </div>
  </div>

  <div class="contact contact-general">
    <div class="row">
      <svg width="18" height="18" viewBox="0 0 20 20"><circle cx="10" cy="10" r="8.5" fill="none" stroke="var(--ink-soft)" stroke-width="1.6"/><ellipse cx="10" cy="10" rx="3.6" ry="8.5" fill="none" stroke="var(--ink-soft)" stroke-width="1.4"/><line x1="1.5" y1="10" x2="18.5" y2="10" stroke="var(--ink-soft)" stroke-width="1.4"/></svg>
      <span>www.krvlane.com</span>
    </div>
    <div class="row">
      <svg width="18" height="13" viewBox="0 0 18 13"><rect x="0.8" y="0.8" width="16.4" height="11.4" fill="none" stroke="var(--ink-soft)" stroke-width="1.6"/><polyline points="1,1 9,7.5 17,1" fill="none" stroke="var(--ink-soft)" stroke-width="1.6"/></svg>
      <span>info@krvsupply.com.au</span>
    </div>
  </div>

</main>
</body>
</html>
```